Your conflict - our mediation - joint conflict SOLUTION

With this flyer I am looking for conflict parties who are ready to tackle and resolve their conflict with a prospective mediator. The mediation is free because I am doing it as part of my diploma thesis. Time frame approx. 4 sessions of 2.5 hours each. The wishes and needs of both parties are listened to and “picked out”. In an open, constructive, appreciative framework, solutions are developed and negotiated together.

Target Market(s)

everyone who is ready to deal with himself and his counterpart and everyone who wants to work out a solution with the respect, openness and support of a mediator.

Requirements
Must have
• - "For my diploma thesis I am looking for conflicting parties who are willing to resolve their conflict with a mediator"
- Time frame: 4 x 2.5 hours feasible in Solothurn, Bern, Brugg
- Free of charge
- my coordinates - see business card
- more information at www.talweidenhof.ch
Nice to have
• the card should be based on the style of my homepage www.talweidenhof.ch and my business card

```html
<!DOCTYPE html>
<html lang="de">
<head>
<meta charset="utf-8">
<title>Mediation Flyer – Talweidenhof</title>
<link rel="stylesheet" href="https://fonts.googleapis.com/css2?family=Source+Sans+3:wght@400;600;700&family=Lobster&display=swap">
<style>
  :root {
    --navy: #2b3a8f;
    --navy-dark: #23307a;
    --green: #1d6a3a;
    --gold: #b8925e;
    --text-grey: #5a5a5a;
    --contact-text: #3b3b55;
    --paper-top: #ffffff;
    --paper-bottom: #e9ebef;
    --page-bg: #d9dadc;
    --sky: #dfe4e8;
    --water: #b9c3c9;
    --deck: #b8a58e;
  }
  * { margin: 0; padding: 0; box-sizing: border-box; }
  html, body { width: 1200px; height: 994px; overflow: hidden; }
  body {
    background: var(--page-bg);
    font-family: "Source Sans 3", "Myriad Pro", Arial, sans-serif;
    position: relative;
  }
  .flyer {
    position: absolute;
    left: 248px; top: 42px;
    width: 704px; height: 910px;
    background: linear-gradient(180deg, var(--paper-top) 45%, var(--paper-bottom) 100%);
    overflow: hidden;
  }
  .hero-photo {
    position: absolute; left: 0; top: 0;
    width: 704px; height: 530px;
    background:
      radial-gradient(ellipse 180px 260px at 520px 200px, rgba(222,214,200,0.9), rgba(222,214,200,0) 70%),
      linear-gradient(180deg, #ffffff 0%, var(--sky) 22%, #c9d0d4 38%, var(--water) 52%, #cfc3b2 70%, var(--deck) 100%);
  }
  .hero-photo::after {
    content: "";
    position: absolute; inset: 0;
    background: linear-gradient(90deg, rgba(255,255,255,0.75) 0%, rgba(255,255,255,0.35) 45%, rgba(255,255,255,0) 70%);
  }
  .hero-wave { position: absolute; left: 0; top: 0; width: 704px; height: 910px; }
  .brand {
    position: absolute; left: 52px; top: 68px;
    display: flex; align-items: center; gap: 10px;
  }
  .brand-dot { width: 16px; height: 16px; border-radius: 50%; background: var(--navy); }
  .brand-name { font-size: 30px; font-weight: 600; color: var(--navy); line-height: 1; }
  .headline {
    position: absolute; left: 36px; top: 168px;
    font-size: 31px; font-weight: 700; color: var(--navy);
    line-height: 38px; text-transform: uppercase;
  }
  .badge { position: absolute; left: 524px; top: 344px; width: 166px; height: 166px; }
  .keywords {
    position: absolute; left: 43px; top: 456px;
    display: flex; align-items: center; gap: 14px;
    font-size: 25px; color: var(--navy); text-transform: uppercase;
  }
  .keywords .tick { width: 16px; height: 16px; margin-right: -6px; }
  .body-copy { position: absolute; left: 0; width: 704px; text-align: center; }
  .claim {
    top: 528px; font-size: 13.5px; font-weight: 700; color: var(--navy-dark);
    text-transform: uppercase; letter-spacing: -0.2px;
  }
  .parties {
    top: 553px; font-size: 13.5px; line-height: 23px; color: var(--text-grey);
  }
  .question { top: 632px; font-size: 23px; font-weight: 700; color: var(--navy); }
  .invitation {
    top: 672px; font-family: "Lobster", cursive; font-size: 20px;
    line-height: 29px; color: var(--green);
  }
  .timeframe { top: 742px; font-size: 15px; color: var(--text-grey); }
  .mediator-name { top: 786px; font-size: 25px; color: var(--navy); text-transform: uppercase; }
  .divider { position: absolute; left: 0; top: 836px; width: 704px; height: 2px; background: var(--navy); }
  .contacts {
    position: absolute; left: 40px; top: 860px; width: 640px;
    display: flex; align-items: center; justify-content: space-between;
    font-size: 21px; color: var(--contact-text);
  }
  .contact-item { display: flex; align-items: center; gap: 12px; }
  .contact-icon { width: 18px; height: 18px; }
</style>
</head>
<body>
  <main class="flyer">
    <div class="hero-photo" role="img" aria-label="Photo: two people meditating back to back on a blanket on a wooden jetty by a mountain lake, sunlight behind them"></div>

    <svg class="hero-wave" viewBox="0 0 704 910" aria-hidden="true">
      <path d="M0,410 C180,360 420,360 704,470 L704,910 L0,910 Z" fill="#e4e6ea"/>
      <path d="M0,440 C200,395 450,410 704,540 L704,910 L0,910 Z" fill="#fafafa"/>
    </svg>

    <div class="brand">
      <span class="brand-dot"></span>
      <span class="brand-name">Talweidenhof</span>
    </div>

    <h1 class="headline">Ihr Konflikt<br>Unsere Mediation<br>Gemeinsame<br>Konfliktlösung</h1>

    <svg class="badge" viewBox="0 0 166 166" aria-label="Free of charge">
      <polygon fill="var(--gold)" points="83,3 94,12 108,7 116,19 131,19 134,33 147,39 145,53 155,63 148,76 153,89 143,99 145,113 132,119 129,133 115,134 107,146 93,142 83,152 73,142 59,146 51,134 37,133 34,119 21,113 23,99 13,89 18,76 11,63 21,53 19,39 32,33 35,19 50,19 58,7 72,12" transform="translate(0,8)"/>
      <text x="83" y="74" text-anchor="middle" font-family="Source Sans 3, sans-serif" font-weight="700" font-size="26" fill="#fff">FREE</text>
      <text x="83" y="98" text-anchor="middle" font-family="Lobster, cursive" font-size="22" fill="#fff">of</text>
      <text x="83" y="126" text-anchor="middle" font-family="Source Sans 3, sans-serif" font-weight="700" font-size="26" fill="#fff">CHARGE</text>
    </svg>

    <div class="keywords">
      <span>Konflikt</span>
      <svg class="tick" viewBox="0 0 16 16" aria-hidden="true"><circle cx="8" cy="8" r="8" fill="var(--green)"/><path d="M4.5,8.2 L7,10.5 L11.5,5.8" fill="none" stroke="#fff" stroke-width="1.8"/></svg>
      <span>Streit</span>
      <svg class="tick" viewBox="0 0 16 16" aria-hidden="true"><circle cx="8" cy="8" r="8" fill="var(--green)"/><path d="M4.5,8.2 L7,10.5 L11.5,5.8" fill="none" stroke="#fff" stroke-width="1.8"/></svg>
      <span>Blockade</span>
    </div>

    <p class="body-copy claim">Mediation&nbsp; - Gemeinsam Lösungen suchen und finden, die alle Parteien mittragen können</p>
    <p class="body-copy parties">mit Ihrer Ehefrau ... Ihrem Vertragspartner ... Ihrer Nachbarin ... Ihrem Mieter ... Ihrer Tochter ... Ihrem<br>Pächter ... Ihrer Schwester ... Ihrem Geschäftspartner ... Ihrer Vorgesetzten ... Ihrem Mitarbeiter ... Ihrem<br>Vater ... Ihrer Vermieterin ... Ihrem Freund ...</p>
    <p class="body-copy question">Sie kommen nicht mehr weiter?</p>
    <p class="body-copy invitation">Ve své diplomové práci hledám konfliktní strany, které jsou ochotny<br>vyřešit jejich konflikt s prostředníkem</p>
    <p class="body-copy timeframe">Časový rámec: 4 x 2,5 hodiny proveditelné v Solothurn, Bern, Brugg</p>
    <p class="body-copy mediator-name">Lea Santoro Meier</p>

    <div class="divider"></div>

    <div class="contacts">
      <span class="contact-item">
        <svg class="contact-icon" viewBox="0 0 18 18" aria-hidden="true"><circle cx="9" cy="9" r="9" fill="var(--navy)"/><g fill="none" stroke="#fff" stroke-width="1"><circle cx="9" cy="9" r="5"/><ellipse cx="9" cy="9" rx="2.2" ry="5"/><line x1="4" y1="9" x2="14" y2="9"/></g></svg>
        talweidenhof.ch
      </span>
      <span class="contact-item">
        <svg class="contact-icon" viewBox="0 0 18 18" aria-hidden="true"><circle cx="9" cy="9" r="9" fill="var(--navy)"/><path d="M6,4.5 L7.6,4.5 L8.4,7 L7.3,7.9 C7.9,9.2 8.8,10.1 10.1,10.7 L11,9.6 L13.5,10.4 L13.5,12 C13.5,12.8 12.8,13.5 12,13.5 C8.3,13.2 4.8,9.7 4.5,6 C4.5,5.2 5.2,4.5 6,4.5 Z" fill="#fff"/></svg>
        078 000 12 34
      </span>
      <span class="contact-item">
        <svg class="contact-icon" viewBox="0 0 18 18" aria-hidden="true"><circle cx="9" cy="9" r="9" fill="var(--navy)"/><rect x="4.5" y="5.8" width="9" height="6.4" fill="#fff"/><path d="M4.5,5.8 L9,9.4 L13.5,5.8" fill="none" stroke="var(--navy)" stroke-width="1"/></svg>
        lsantoro@mailbox.ch
      </span>
    </div>
  </main>
</body>
</html>
```